Velora "Glass Tide" single cover

We need a cover for Velora's New upcoming single "Glass Tide"
We have posted some Pictures and logo that we want you to work With. We need you to get her to look good :).The title is "Glass Tide" and is "Velora feat. Dorvo mint rascal"
The songs is a little hiphop/RnB (Marla Q'ish).
You can choose what colour you want for the logo and overall. But we don't want it to be gloomy.
watch www.velora-music.example or www.facebook.com/veloramusic
This is a digital release so we need only front page 12x12cm
Updates
If anyone wants to remove the background from the pictures and be creative that is fine! :)
Industry/Entity Type
Digital
Colors
Designer to choose colors to be used in the design.
Look and feel
Each slider illustrates characteristics of the customer's brand and the style your logo design should communicate.

```html
<!DOCTYPE html>
<html lang="en">
<head>
<meta charset="utf-8">
<title>Velora – Glass Tide</title>
<link rel="stylesheet" href="https://fonts.googleapis.com/css2?family=Open+Sans:wght@700;800&family=Ultra&display=swap">
<style>
  :root {
    --paper: #ffffff;
    --pink: #f0287a;
    --pink-deep: #b8155a;
    --pink-dark: #8a0c42;
    --photo-top: #8a6a52;
    --photo-bottom: #1c1a1c;
    --glow: rgba(240, 40, 122, 0.16);
  }
  * { margin: 0; padding: 0; box-sizing: border-box; }
  html, body {
    width: 1200px;
    height: 1200px;
    overflow: hidden;
    background: var(--paper);
  }
  .cover {
    position: relative;
    width: 1200px;
    height: 1200px;
    background: var(--paper);
    overflow: hidden;
  }
  .artist-name {
    position: absolute;
    left: 0;
    right: 0;
    top: -12px;
    text-align: center;
    font-family: "Open Sans", Arial, sans-serif;
    font-weight: 800;
    font-size: 340px;
    line-height: 1;
    letter-spacing: -6px;
    color: var(--pink);
    z-index: 3;
  }
  .featuring {
    position: absolute;
    right: 34px;
    top: 306px;
    font-family: "Open Sans", Arial, sans-serif;
    font-weight: 700;
    font-size: 36px;
    line-height: 1;
    color: var(--pink);
    z-index: 3;
  }
  .portrait {
    position: absolute;
    left: 254px;
    top: 360px;
    width: 760px;
    height: 560px;
    border-radius: 24px;
    background: linear-gradient(180deg, var(--photo-top) 0%, #3a302c 45%, var(--photo-bottom) 100%);
    z-index: 1;
  }
  .title-glow {
    position: absolute;
    left: 40px;
    top: 1000px;
    width: 1120px;
    height: 150px;
    background: radial-gradient(ellipse at center, var(--glow), transparent 70%);
    z-index: 1;
  }
  .single-title {
    position: absolute;
    left: 0;
    right: 0;
    top: 862px;
    text-align: center;
    font-family: "Ultra", "Rockwell", serif;
    font-weight: 400;
    font-size: 190px;
    line-height: 1;
    letter-spacing: 16px;
    color: var(--pink);
    white-space: nowrap;
    z-index: 2;
    text-shadow:
      2px 2px 0 var(--pink-deep),
      4px 4px 0 var(--pink-deep),
      6px 6px 0 var(--pink-deep),
      8px 8px 0 var(--pink-dark),
      10px 10px 0 var(--pink-dark),
      18px 24px 22px rgba(0, 0, 0, 0.25);
  }
</style>
</head>
<body>
  <main class="cover">
    <h1 class="artist-name">velora</h1>
    <p class="featuring">feat. Dorvo mint rascal</p>

    <div class="portrait" role="img" aria-label="Photo of the singer seated on the floor in a black leather jacket and ripped black leggings"></div>

    <div class="title-glow"></div>
    <h2 class="single-title">Glass Tide</h2>
  </main>
</body>
</html>
```